Stationary Design needed for luxorious bespoke tailor

We need a design for our stationary items like businescards, letters, envelope and letter head / Signature for email. Our company "LE CORVAN" sells exclusively and luxourious bespoke garments and accessories for men. The desgins of letterhead, envelope and business card shoulderstand communicate luxury, high quality and good taste. We would like our logo to be used on the designs.

Target Market(s)

Gentleman with a high aproach and exclusive and luxourious suits and shirts, grooms, businesman,

Industry/Entity Type

It Company

Font styles to use
Sans Serif

Colors
ec1f27
ffffff

Requirements
Must have
• Logo, Companies name and adress, contactName internet & email, phone number line / mobile, VAT Nr. On Business Card frontpage only logo and name, adress companies on backpage. No VAT and Companies ID there. Company data; LE CORVAN AG Wiesenrain 42 4057 Basel Switzerland VAT: CHE 472 916 304 Tax Tel 41 61 594 17 36 Mobile 41 79 842 06 91 www.korvanmode.ch info@korvanmode.com.
Nice to have
• -Name And phone numbers need to be able to change (for different coworkers ...)
Should not have
• no VAT in Business Card

```html
<!DOCTYPE html>
<html lang="de">
<head>
<meta charset="utf-8">
<title>LE CORVAN – Visitenkarte</title>
<link href="https://fonts.googleapis.com/css2?family=Montserrat:wght@400;500;600;700&display=swap" rel="stylesheet">
<style>
  :root {
    --backdrop: #2b2b2b;
    --card-black: #0a0a0a;
    --card-white: #ffffff;
    --brand-red: #ec1f27;
    --ink: #1a1a1a;
    --ink-soft: #3a3a3a;
  }
  * { margin: 0; padding: 0; box-sizing: border-box; }
  html, body {
    width: 1200px;
    height: 672px;
    overflow: hidden;
  }
  body {
    background: var(--backdrop);
    font-family: "Montserrat", sans-serif;
    position: relative;
  }
  .card {
    position: absolute;
    top: 186px;
    width: 500px;
    height: 300px;
    box-shadow: 0 10px 30px rgba(0,0,0,.45);
  }
  .card--front {
    left: 60px;
    background: var(--card-black);
    display: flex;
    align-items: center;
    justify-content: center;
  }
  .card--front .brand-name {
    color: var(--card-white);
    font-size: 54px;
    font-weight: 600;
    letter-spacing: 4px;
  }
  .card--back {
    left: 640px;
    background: var(--card-white);
    color: var(--ink);
  }
  .card--back .brand-name {
    position: absolute;
    left: 130px;
    top: 40px;
    font-size: 28px;
    font-weight: 600;
    letter-spacing: 2px;
    color: var(--ink);
  }
  .person {
    position: absolute;
    left: 40px;
    top: 150px;
  }
  .person-name {
    font-size: 13px;
    font-weight: 700;
    letter-spacing: .5px;
  }
  .person-role {
    font-size: 8px;
    font-weight: 600;
    letter-spacing: .4px;
    margin-top: 2px;
  }
  .contact {
    position: absolute;
    left: 40px;
    right: 30px;
    top: 212px;
    font-size: 10.5px;
    color: var(--ink-soft);
    font-weight: 500;
  }
  .contact-line { white-space: nowrap; }
  .contact .label { color: var(--brand-red); font-weight: 600; }
  .contact .sep { margin: 0 5px; }
  .contact-rule {
    height: 1px;
    background: var(--brand-red);
    margin: 8px 0 8px;
  }
</style>
</head>
<body>
  <section class="card card--front" aria-label="Visitenkarte Vorderseite">
    <span class="brand-name">LE CORVAN</span>
  </section>

  <section class="card card--back" aria-label="Visitenkarte Rückseite">
    <span class="brand-name">LE CORVAN</span>

    <div class="person">
      <p class="person-name">JONAS MEIER</p>
      <p class="person-role">MANAGING DIRECTOR</p>
    </div>

    <div class="contact">
      <p class="contact-line">
        <span class="label">t:</span> +41 61 594 17 36<span class="sep">|</span><span class="label">m:</span> +41 79 842 06 91<span class="sep">|</span><span class="label">e:</span> info@korvanmode.com
      </p>
      <div class="contact-rule"></div>
      <p class="contact-line">
        <span class="label">w:</span> www.korvanmode.com<span class="sep">|</span>Wiesenrain 42 - 4057 Basel - Switzerland
      </p>
    </div>
  </section>
</body>
</html>
```